Cover Photo Design Needed for Business

We need a Facebook cover photo design for a new company called "Quillandermoor". Our goal is to enable your success through the free exchange of wisdom and tools through other entrepreneur's. For those looking to take further steps, we offer several paid services that can help you start, manage, and grow your venture. Were looking for something new and creative.

Industry/Entity Type

Business

Requirements
Nice to have
• If it goes with the cover photo we would like an arrow pointing to the like button.

```html
<!DOCTYPE html>
<html lang="en">
<head>
<meta charset="utf-8">
<title>Quillandermoor – Cover</title>
<link href="https://fonts.googleapis.com/css2?family=Arimo:wght@400;700&display=swap" rel="stylesheet">
<style>
  :root {
    --green: #a6cc3c;
    --green-dark: #7fa52a;
    --icon: #6e8a26;
    --label-top: #8a8a8a;
    --label-bottom: #5e5e5e;
    --text-grey: #7d7d7d;
    --brand-grey: #8c8c8c;
    --rule: #8f8f8f;
    --backdrop-centre: #ffffff;
    --backdrop-edge: #ececec;
    --soil: #332d26;
    --skin: #d3a78b;
    --white: #ffffff;
    --btn-border: #9a9a9a;
    --btn-text: #333333;
  }
  * { margin: 0; padding: 0; box-sizing: border-box; }
  html, body { width: 1200px; height: 564px; overflow: hidden; background: var(--white); }
  body { font-family: "Arimo", Arial, sans-serif; position: relative; }

  .cover {
    position: absolute; left: 0; top: 0; width: 1200px; height: 444px;
    background: radial-gradient(ellipse at 690px 200px, var(--backdrop-centre) 0%, var(--backdrop-edge) 100%);
    border-bottom: 1px solid var(--rule);
    overflow: hidden;
  }
  .hand-photo {
    position: absolute; left: 0; top: 0; width: 530px; height: 400px;
    background: linear-gradient(175deg, var(--backdrop-edge) 0%, var(--soil) 30%, var(--soil) 52%, var(--skin) 72%, var(--skin) 100%);
    -webkit-mask-image: linear-gradient(90deg, #000 70%, transparent 100%);
            mask-image: linear-gradient(90deg, #000 70%, transparent 100%);
  }

  .services { position: absolute; top: 20px; left: 567px; display: flex; gap: 28px; }
  .service { width: 155px; height: 241px; display: flex; flex-direction: column; }
  .service-icon {
    height: 184px; background: var(--green); position: relative;
    display: flex; align-items: center; justify-content: center;
  }
  .service-icon::after {
    content: ""; position: absolute; bottom: -8px; left: 50%; margin-left: -8px;
    border-left: 8px solid transparent; border-right: 8px solid transparent; border-top: 8px solid var(--green);
    z-index: 2;
  }
  .service-label {
    flex: 1; background: linear-gradient(var(--label-top), var(--label-bottom));
    color: var(--white); font-weight: 700; font-size: 19px;
    display: flex; align-items: center; justify-content: center;
  }

  .tagline {
    position: absolute; left: 560px; width: 540px; top: 270px;
    text-align: center; color: var(--text-grey); font-weight: 700; font-size: 20px; line-height: 24px;
  }
  .pointer { position: absolute; left: 835px; top: 360px; }

  .wordmark {
    position: absolute; left: 280px; top: 396px;
    font-size: 36px; font-weight: 400; color: var(--brand-grey); line-height: 40px;
  }

  .profile {
    position: absolute; left: 27px; top: 275px; width: 239px; height: 237px;
    background: var(--white); border: 1px solid #c8c8c8;
    display: flex; flex-direction: column; align-items: center; justify-content: center; gap: 14px;
  }
  .profile-dot { width: 120px; height: 120px; border-radius: 50%; background: var(--green); }
  .profile-name { font-size: 22px; font-weight: 700; color: var(--brand-grey); }

  .actions { position: absolute; top: 468px; left: 897px; display: flex; gap: 14px; }
  .btn {
    height: 33px; border: 1px solid var(--btn-border); border-radius: 2px;
    background: linear-gradient(#ffffff, #ececec);
    font-weight: 700; font-size: 17px; color: var(--btn-text);
    display: flex; align-items: center;
  }
  .btn-like { width: 91px; justify-content: center; gap: 7px; }
  .btn-like .mark { width: 12px; height: 12px; background: #5d6d8f; }
  .btn-message { width: 171px; }
  .btn-message .text { flex: 1; text-align: center; }
  .btn-message .menu {
    width: 59px; height: 100%; border-left: 1px solid var(--btn-border);
    display: flex; align-items: center; justify-content: center; gap: 6px;
  }
</style>
</head>
<body>
  <section class="cover">
    <div class="hand-photo" role="img" aria-label="Photo of an open hand holding dark soil with a young green seedling"></div>

    <div class="services">
      <div class="service">
        <div class="service-icon">
          <svg width="56" height="56" viewBox="0 0 56 56" aria-hidden="true">
            <polygon points="4,8 52,28 24,32" fill="var(--icon)"/>
            <polygon points="24,32 52,28 30,52" fill="#5a7220"/>
          </svg>
        </div>
        <div class="service-label">START</div>
      </div>
      <div class="service">
        <div class="service-icon">
          <svg width="64" height="64" viewBox="0 0 64 64" aria-hidden="true">
            <g fill="var(--icon)">
              <rect x="27" y="4" width="10" height="56" rx="2"/>
              <rect x="27" y="4" width="10" height="56" rx="2" transform="rotate(45 32 32)"/>
              <rect x="27" y="4" width="10" height="56" rx="2" transform="rotate(90 32 32)"/>
              <rect x="27" y="4" width="10" height="56" rx="2" transform="rotate(135 32 32)"/>
              <circle cx="32" cy="32" r="20"/>
            </g>
            <circle cx="32" cy="32" r="8" fill="var(--green)"/>
          </svg>
        </div>
        <div class="service-label">MANAGE</div>
      </div>
      <div class="service">
        <div class="service-icon">
          <svg width="40" height="76" viewBox="0 0 40 76" aria-hidden="true">
            <g fill="none" stroke="var(--icon)" stroke-width="4" stroke-linecap="round">
              <path d="M12 4 h16 M10 12 h20 M10 20 h20 M10 28 h20 M12 36 h16"/>
            </g>
            <path d="M6 42 h28 v10 a14 12 0 0 1 -28 0 z" fill="var(--icon)"/>
            <rect x="14" y="64" width="12" height="8" rx="2" fill="var(--icon)"/>
          </svg>
        </div>
        <div class="service-label">GROW</div>
      </div>
    </div>

    <p class="tagline">Achieve success through<br>the free exchange of wisdom and tools<br>through other entrepreneur's.</p>

    <svg class="pointer" width="110" height="84" viewBox="0 0 110 84" aria-hidden="true">
      <path d="M8 10 C40 4, 78 24, 92 66" fill="none" stroke="var(--green-dark)" stroke-width="6" stroke-linecap="round"/>
      <path d="M76 58 L94 74 L104 50" fill="none" stroke="var(--green-dark)" stroke-width="6" stroke-linecap="round" stroke-linejoin="round"/>
    </svg>

    <div class="wordmark">Quillandermoor</div>
  </section>

  <div class="profile">
    <div class="profile-dot"></div>
    <div class="profile-name">Quillandermoor</div>
  </div>

  <div class="actions">
    <div class="btn btn-like"><span class="mark"></span>Like</div>
    <div class="btn btn-message">
      <span class="text">Message</span>
      <span class="menu">
        <svg width="14" height="14" viewBox="0 0 14 14" aria-hidden="true"><circle cx="7" cy="7" r="5" fill="none" stroke="#555" stroke-width="3" stroke-dasharray="2 1.5"/></svg>
        <svg width="12" height="8" viewBox="0 0 12 8" aria-hidden="true"><polygon points="0,0 12,0 6,7" fill="#4a6aa5"/></svg>
      </span>
    </div>
  </div>
</body>
</html>
```